Sports Nutrition Supplement Label design

We need a sports supplement label design for an existing business. (I have provided our business logo in the file uploads) These labels will remain consistent across the product line with the name of the product being the only changing field. The current product names (example: "vegan") on the labels provided are just for reference, the ingredients portions etc are final, but the actual name will be changed to something less generic for each product. I will just need to be able to change the name and have it match with label concept. We would like the look to be professional, clean, and exemplify quality. Please reference our business website tidelinevigor.com to get a feel for design and brand association.
I have also included the NKB supplement label guidelines so we are certain to maintain compliance.
Thank you and I'm looking forward to working with you and seeing your creative designs!
Darin

Target Market(s)

Athletes, Sports professionals, Colleges, Professional Sports Teams

Industry/Entity Type

Sports Science/ Sports Training/Athletics

Requirements
Nice to have
• I would like the design to possibly reflect these key terms: Sport Science, Chemistry, Clean, Professional, Quality (We also like water/ocean/waves concepts but is not a "requirement" it would have to really work well in the design somehow to appeal to wide range of athletes)

```html
<!DOCTYPE html>
<html lang="en">
<head>
<meta charset="utf-8">
<title>Tideline Vigor – Vegan Protein Label</title>
<link rel="stylesheet" href="https://fonts.googleapis.com/css2?family=Montserrat:wght@500;700;800&family=Open+Sans:wght@400;600;700&family=Roboto+Condensed:wght@400&display=swap">
<style>
  :root {
    --page: #ffffff;
    --label: #0b0b0b;
    --ink-light: #ffffff;
    --ink-dark: #111111;
    --glow-red: #8a0f12;
    --badge-green: #1f8a3a;
    --badge-blue: #2a6fb0;
    --badge-grey: #8b8f96;
    --faint: #2a2a2a;
  }
  * { box-sizing: border-box; margin: 0; padding: 0; }
  html, body { width: 1200px; height: 1200px; overflow: hidden; background: var(--page); }
  body { position: relative; font-family: "Open Sans", sans-serif; }

  .label {
    position: absolute; left: 0; top: 405px;
    width: 1200px; height: 389px;
    background: var(--label); color: var(--ink-light); overflow: hidden;
  }
  .label__glow {
    position: absolute; left: 300px; top: 40px; width: 600px; height: 340px;
    background: radial-gradient(ellipse at 50% 55%, rgba(138,15,18,.55) 0%, rgba(138,15,18,.18) 45%, rgba(11,11,11,0) 72%);
  }

  /* left panel */
  .story { position: absolute; left: 36px; top: 13px; width: 222px; font-size: 8px; line-height: 11px; }
  .story p + p { margin-top: 6px; }
  .box { position: absolute; left: 36px; width: 218px; background: #fff; color: var(--ink-dark); padding: 2px 3px; }
  .usage { top: 145px; height: 28px; font-size: 6.4px; line-height: 1.35; }
  .amino { top: 181px; height: 95px; font-size: 5px; line-height: 1.55; padding: 2px 3px 3px; }
  .amino__title { text-align: center; font-size: 5.3px; border-bottom: .6px solid #111; padding-bottom: 1px; margin-bottom: 1px; }
  .amino__cols { display: grid; grid-template-columns: 1fr 1fr; column-gap: 10px; }
  .amino__row { display: flex; }
  .amino__row .dots { flex: 1; border-bottom: .6px dotted #333; margin: 0 2px 2px; }
  .amino__total { border-top: .6px solid #111; margin-top: 1px; padding-top: 1px; width: 50%; }
  .disclaimer { top: 282px; height: 27px; font-size: 5.2px; font-weight: 700; line-height: 1.35; }
  .badges { position: absolute; left: 36px; top: 316px; display: flex; gap: 12px; }
  .badge { width: 34px; height: 34px; border-radius: 50%; }
  .badge--blue { background: var(--badge-blue); }
  .badge--green { background: var(--badge-green); }
  .badge--grey { background: var(--badge-grey); }
  .lot { position: absolute; left: 36px; top: 357px; font-size: 7.4px; color: var(--faint); }
  .sku { position: absolute; left: 36px; top: 369px; font-size: 9px; font-weight: 700; }

  /* centre panel */
  .brand {
    position: absolute; left: 0; width: 1200px; top: 50px; text-align: center;
    font-family: "Montserrat", sans-serif; font-weight: 500; font-size: 30px; letter-spacing: 8px;
  }
  .product {
    position: absolute; left: 0; width: 1200px; top: 130px; text-align: center;
    font-family: "Montserrat", sans-serif; font-weight: 800; font-size: 114px; line-height: 1; letter-spacing: -2px;
  }
  .flavour {
    position: absolute; left: 0; width: 1200px; top: 256px; text-align: center;
    font-family: "Montserrat", sans-serif; font-weight: 800; font-size: 26px; line-height: .95;
  }
  .flavour__note { display: block; font-size: 14.5px; font-weight: 700; margin-top: 7px; letter-spacing: .5px; }
  .netwt {
    position: absolute; left: 0; width: 1200px; top: 350px; text-align: center;
    font-family: "Roboto Condensed", sans-serif; font-size: 11.5px;
  }
  .netwt .sep { display: inline-block; width: 1px; height: 14px; background: #fff; vertical-align: middle; margin: 0 6px; }
  .vegan-seal { position: absolute; left: 853px; top: 294px; }

  /* facts panel */
  .facts {
    position: absolute; left: 991px; top: 9px; width: 175px; background: #fff; color: var(--ink-dark);
    padding: 3px 4px; font-size: 6.2px; line-height: 1.2;
  }
  .facts__title { font-family: "Open Sans", sans-serif; font-weight: 700; font-size: 18.5px; line-height: 1.05; letter-spacing: -.5px; white-space: nowrap; }
  .facts__serving { font-size: 9px; line-height: 1.2; border-bottom: 3.5px solid #111; padding-bottom: 1px; }
  .facts__head { display: flex; justify-content: space-between; font-weight: 700; font-size: 5.4px; border-bottom: 1.5px solid #111; padding: 2px 0 1px; }
  .facts__row { display: grid; grid-template-columns: 1fr 36px 30px; border-bottom: .5px solid #444; padding: 1.4px 0; }
  .facts__row span:nth-child(2), .facts__row span:nth-child(3) { text-align: right; }
  .facts__row--indent span:first-child { padding-left: 4px; }
  .facts__row--indent2 span:first-child { padding-left: 11px; }
  .facts__row--thick { border-bottom: 1.5px solid #111; }
  .facts__blend { border-bottom: .5px solid #444; padding: 1.4px 0; }
  .facts__blend .facts__row { border: 0; padding: 0; }
  .facts__blend p { padding-left: 3px; }
  .facts__foot { border-top: 2.5px solid #111; font-size: 4.8px; padding-top: 1px; }
  .ingredients { position: absolute; left: 986px; top: 316px; width: 178px; font-size: 6px; line-height: 8.6px; }
  .distributor { position: absolute; left: 986px; top: 352px; font-size: 7.3px; font-weight: 700; line-height: 10px; }
</style>
</head>
<body>
<section class="label">
  <div class="label__glow" role="img" aria-label="Dark red diagonal light streaks behind the product name"></div>

  <div class="story">
    <p>If you are looking for a healthier alternative to animal-based protein you have found it! Vegan protein is made up of three vegan proteins; Quinoa, Brown Rice and Pea Isolate. These provide amino acids, vitamins, and the minerals that your body needs. They are also higher in fiber which will aid in weight management.</p>
    <p>Vegan Protein contains no artificial sweeteners, colors or flavors. This, along with the protein blend, will help relieve stress on your digestive system. A blend of eleven different super fruits provides antioxidants to help you with your overall health.</p>
  </div>

  <div class="box usage"><b>Suggested Use</b>: Mix one heaping scoop with 4-6oz of water, milk, or your favorite beverage. Vary the amount of liquid for taste preference.</div>

  <div class="box amino">
    <div class="amino__title">Approximate Amino Acids per Serving (Naturally Occurring)</div>
    <div class="amino__cols">
      <div>
        <div class="amino__row"><span>Alanine</span><span class="dots"></span><span>850 mg</span></div>
        <div class="amino__row"><span>Aspartic Acid</span><span class="dots"></span><span>2180 mg</span></div>
        <div class="amino__row"><span>Glutamic Acid</span><span class="dots"></span><span>3240 mg</span></div>
        <div class="amino__row"><span>Histidine</span><span class="dots"></span><span>501 mg</span></div>
        <div class="amino__row"><span>Leucine*</span><span class="dots"></span><span>1670 mg</span></div>
        <div class="amino__row"><span>Methionine</span><span class="dots"></span><span>189 mg</span></div>
        <div class="amino__row"><span>Proline</span><span class="dots"></span><span>898 mg</span></div>
        <div class="amino__row"><span>Threonine</span><span class="dots"></span><span>709 mg</span></div>
        <div class="amino__row"><span>Tyrosine</span><span class="dots"></span><span>676 mg</span></div>
      </div>
      <div>
        <div class="amino__row"><span>Arginine</span><span class="dots"></span><span>1565 mg</span></div>
        <div class="amino__row"><span>Cystine</span><span class="dots"></span><span>184 mg</span></div>
        <div class="amino__row"><span>Glycine</span><span class="dots"></span><span>3127 mg</span></div>
        <div class="amino__row"><span>Isoleucine*</span><span class="dots"></span><span>929 mg</span></div>
        <div class="amino__row"><span>Lysine</span><span class="dots"></span><span>1403 mg</span></div>
        <div class="amino__row"><span>Phenylalanine</span><span class="dots"></span><span>1055 mg</span></div>
        <div class="amino__row"><span>Serine</span><span class="dots"></span><span>900 mg</span></div>
        <div class="amino__row"><span>Tryptophan</span><span class="dots"></span><span>157 mg</span></div>
        <div class="amino__row"><span>Valine*</span><span class="dots"></span><span>1030 mg</span></div>
      </div>
    </div>
    <div class="amino__row amino__total"><span>Total BCAAs</span><span class="dots"></span><span>3629 mg</span></div>
  </div>

  <div class="box disclaimer">* These statements have not been evaluated by the NKB. This product is not intended to diagnose, treat, cure or prevent any disease.</div>

  <div class="badges">
    <span class="badge badge--blue"></span>
    <span class="badge badge--green"></span>
    <span class="badge badge--blue"></span>
    <span class="badge badge--grey"></span>
    <span class="badge badge--green"></span>
  </div>
  <p class="lot">Lot # and Expiration Date Printed on Bottom of Bottle.</p>
  <p class="sku">SKU:TLV418K</p>

  <p class="brand">TIDELINE VIGOR</p>
  <h1 class="product">VEGAN</h1>
  <p class="flavour">CHOCOLATE<br>MILKSHAKE<span class="flavour__note">NATURAL &nbsp;FLAVOR</span></p>
  <p class="netwt">NET WT. &nbsp;907 G &nbsp;(2 LB)<span class="sep"></span>DIETARY SUPPLEMENT</p>
  <svg class="vegan-seal" width="64" height="64" viewBox="0 0 64 64" aria-hidden="true">
    <circle cx="32" cy="32" r="30" fill="none" stroke="var(--badge-green)" stroke-width="3"/>
    <circle cx="32" cy="32" r="20" fill="none" stroke="var(--badge-green)" stroke-width="2"/>
  </svg>

  <div class="facts">
    <div class="facts__title">Supplement Facts</div>
    <div class="facts__serving">Serving Size: 32g<br>Servings Per Container: 28</div>
    <div class="facts__head"><span>Amount Per Serving</span><span>% Daily Value**</span></div>
    <div class="facts__row facts__row--thick"><span>Calories &nbsp;140</span><span></span><span></span></div>
    <div class="facts__row"><span>Total Fat</span><span>3 g</span><span>4%</span></div>
    <div class="facts__row facts__row--indent"><span>Saturated Fat</span><span>1 g</span><span>5%</span></div>
    <div class="facts__row"><span>Sodium</span><span>310 mg</span><span>14%</span></div>
    <div class="facts__row"><span>Total Carbohydrate</span><span>6 g</span><span>2%</span></div>
    <div class="facts__row facts__row--indent"><span>Dietary Fiber</span><span>2 g</span><span>7%</span></div>
    <div class="facts__row facts__row--indent"><span>Total Sugars</span><span>2 g</span><span></span></div>
    <div class="facts__row facts__row--indent2"><span>Includes 2g Added Sugars</span><span></span><span>4%</span></div>
    <div class="facts__row"><span>Protein</span><span>20 g</span><span>41%</span></div>
    <div class="facts__row"><span>Vitamin D</span><span>0 mcg</span><span>0%</span></div>
    <div class="facts__row"><span>Calcium</span><span>34 mg</span><span>2%</span></div>
    <div class="facts__row"><span>Iron</span><span>6 mg</span><span>35%</span></div>
    <div class="facts__row facts__row--thick"><span>Potassium</span><span>57 mg</span><span>2%</span></div>
    <div class="facts__blend">
      <div class="facts__row"><span>Vegan Protein Blend</span><span>25 g</span><span>‡</span></div>
      <p>(Pea Protein Isolate, Brown Rice Protein, Quinoa)</p>
    </div>
    <div class="facts__blend">
      <div class="facts__row"><span>MCT Oil Powder</span><span>400 mg</span><span>‡</span></div>
      <p>(Natural MCT Oil, Maltodextrin, Modified Food Starch)</p>
    </div>
    <div class="facts__blend">
      <div class="facts__row"><span>Antioxidant Blend</span><span>150 mg</span><span>‡</span></div>
      <p>(Acai Berry, Acerola, Amla, Jabuticaba, Cranberry, Goji, Mangosteen, Maqui Berry, Pomegranate, Strawberry, Organic Schisandra)</p>
    </div>
    <div class="facts__foot">**Percent Daily Values are based on a 2,000 calorie diet.<br>‡Daily Value not established.</div>
  </div>

  <p class="ingredients"><b>Other Ingredients:</b> Creamer (High Oleic Sunflower Oil, Tapioca Starch, Tapioca Dextrin, Natural Flavors, D Alpha Tocopherols), Raw Sugar, Natural Flavors, Cocoa (processed with alkali), Stevia, Xanthan Gum.</p>
  <p class="distributor">Distributed By: Company Name<br>Street Address City, ST Zipcode<br>website or phone number</p>
</section>
</body>
</html>
```